VORTEQ

It’s is a startup business. We design and build new products.

Target Market(s)

For my first two products, they are targeting the laundry market, hanger accessory, and new modern style clothes dryer. I also have a Pet Treat product at patent stage, and there are other products not yet started but will be more engineering based. Therefore from young adults to older population

Industry/Entity Type

Colours of website to match the logo (att)

Coding

Coded - Design and coding required

Number of Pages Required

1 page

Font styles to use
Other font styles liked:
• Some of the same font as the logo

Colors

Designer to choose colors to be used in the design.

Requirements
Must have
• An upbeat vibe - the logo looks great so inline with that !
Should not have
• anything old fashioned and old style fonts

```html
<!DOCTYPE html>
<html lang="en">
<head>
<meta charset="utf-8">
<title>VORTEQ — Innovation & Technical Services</title>
<link href="https://fonts.googleapis.com/css2?family=Orbitron:wght@500;700;800&family=Open+Sans:wght@400;600&display=swap" rel="stylesheet">
<style>
:root{
  --navy:#1f2f8f;
  --indigo:#2e3a9c;
  --cyan:#00a9d6;
  --aqua:#00d6d6;
  --sky:#1bb8e8;
  --ink:#111111;
  --text:#3a3a3a;
  --white:#ffffff;
  --footer:#3d3d3f;
  --hero-dark:#06142a;
  --hero-mid:#0b3766;
  --display:'Orbitron', sans-serif;
  --body:'Open Sans', sans-serif;
}
*{box-sizing:border-box;margin:0;padding:0}
html,body{width:1200px;height:3424px;overflow:hidden;background:var(--white)}
.page{position:relative;width:1200px;height:3424px;overflow:hidden;font-family:var(--body);color:var(--text)}
.abs{position:absolute}
.display{font-family:var(--display);text-transform:uppercase;letter-spacing:1px}

/* header */
.site-header{position:absolute;left:0;top:0;width:1200px;height:98px;background:var(--white)}
.brand{position:absolute;left:113px;top:22px}
.brand-name{font-family:var(--display);font-weight:500;font-size:34px;letter-spacing:6px;color:var(--navy);line-height:1}
.brand-tag{font-family:var(--display);font-size:8px;letter-spacing:2px;color:var(--navy);margin-top:6px;text-transform:uppercase}
.nav{position:absolute;top:39px;left:0;width:1200px}
.nav a{position:absolute;font-family:var(--display);font-weight:800;font-size:13px;letter-spacing:1.5px;color:var(--ink);text-decoration:none;text-transform:uppercase}
.nav a.active{color:var(--navy)}

/* hero */
.hero{position:absolute;left:0;top:98px;width:1200px;height:554px;border-bottom-right-radius:215px;overflow:hidden;
  background:radial-gradient(circle at 72% 42%, #1f7fd0 0%, var(--hero-mid) 28%, var(--hero-dark) 68%)}
.hero-title{position:absolute;left:121px;top:128px;font-family:var(--display);font-weight:700;font-size:29px;line-height:35px;letter-spacing:3px;color:var(--sky);text-transform:uppercase}
.hero-sub{position:absolute;left:124px;top:254px;font-family:var(--display);font-weight:700;font-size:12.5px;line-height:19px;letter-spacing:1.5px;color:var(--white);text-transform:uppercase}
.btn{position:absolute;display:flex;align-items:center;justify-content:center;font-family:var(--display);font-weight:800;letter-spacing:1.5px;color:var(--white);text-transform:uppercase;
  background:linear-gradient(90deg,var(--aqua) 0%,var(--cyan) 45%,var(--indigo) 100%);border-radius:22px 30px 30px 0}
.btn-hero{left:125px;top:338px;width:381px;height:56px;font-size:13px}

/* about */
.about-visual{position:absolute;left:120px;top:759px;width:455px;height:508px;border-bottom-left-radius:175px;
  background:radial-gradient(circle at 50% 55%, #d6f6ff 0%, #38b4d4 30%, #0f6a8c 65%, #083a52 100%)}
.section-title{font-family:var(--display);font-weight:700;text-transform:uppercase;letter-spacing:4px;color:var(--ink)}
.about-title{position:absolute;left:662px;top:790px;font-size:38px}
.about-sub{position:absolute;left:662px;top:852px;font-family:var(--display);font-weight:800;font-size:19px;line-height:26px;letter-spacing:2px;color:var(--ink);text-transform:uppercase}
.about-copy{position:absolute;left:662px;top:948px;width:420px;font-size:17.5px;line-height:26px;color:var(--text)}
.about-copy p+p{margin-top:25px}
.btn-read{left:658px;top:1180px;width:185px;height:55px;font-size:12px}

/* products */
.products{position:absolute;left:0;top:1386px;width:1200px;height:680px;border-top-left-radius:135px;
  background:linear-gradient(180deg,var(--cyan) 0%,#06aee0 60%,#2ab7ea 100%)}
.products-title{position:absolute;left:0;top:140px;width:1200px;text-align:center;font-size:44px;color:var(--white)}
.card{position:absolute;top:234px;width:313px;height:320px;border-radius:20px;overflow:hidden;background:var(--white)}
.card-photo{position:absolute;left:0;top:0;width:313px;height:241px;border-radius:20px 20px 20px 20px}
.card-name{position:absolute;left:22px;top:264px;font-family:var(--display);font-weight:800;font-size:17px;line-height:26px;letter-spacing:2px;color:var(--ink);text-transform:uppercase}
.card-open{background:linear-gradient(160deg,#4a4fc4 0%,#3d45b8 60%,#3540a8 100%)}
.card-open h3{position:absolute;left:22px;top:46px;font-family:var(--display);font-weight:800;font-size:17px;line-height:26px;letter-spacing:2px;color:var(--white);text-transform:uppercase}
.card-open p{position:absolute;left:24px;top:118px;width:270px;font-size:17px;line-height:26px;color:var(--white)}
.ribbon{position:absolute;left:-40px;top:42px;width:210px;height:30px;background:var(--aqua);transform:rotate(-45deg);
  font-family:var(--body);font-weight:600;font-size:12px;letter-spacing:1px;color:var(--ink);display:flex;align-items:center;justify-content:center;text-transform:uppercase}

/* why choose */
.why-title{position:absolute;left:160px;top:2240px;font-size:34px;line-height:36px}
.feature{position:absolute;left:114px;width:520px;height:80px}
.feature-icon{position:absolute;left:0;top:0;width:72px;height:72px}
.feature h4{position:absolute;left:95px;top:2px;font-family:var(--display);font-weight:800;font-size:16px;letter-spacing:2px;color:var(--cyan);text-transform:uppercase}
.feature p{position:absolute;left:95px;top:28px;width:420px;font-size:17.5px;line-height:26px;color:var(--text)}
.btn-join{left:209px;top:2642px;width:277px;height:55px;font-size:12px}
.why-visual{position:absolute;left:650px;top:2202px;width:436px;height:537px;
  background:linear-gradient(160deg,#6b5a45 0%,#1f3340 45%,#0c4a5a 75%,#1a7a88 100%)}

/* footer */
.site-footer{position:absolute;left:0;top:2941px;width:1200px;height:483px;background:var(--footer);border-top-right-radius:135px}
.footer-brand{position:absolute;left:0;top:110px;width:1200px;text-align:center}
.footer-brand .brand-name{color:var(--white);font-size:48px;letter-spacing:10px}
.footer-brand .brand-tag{color:var(--white);font-size:11px;letter-spacing:3px;margin-top:10px}
.contact{position:absolute;top:248px;height:72px}
.contact-icon{position:absolute;left:0;top:0;width:72px;height:72px}
.contact h5{position:absolute;left:92px;top:8px;font-family:var(--display);font-weight:800;font-size:15px;letter-spacing:2px;color:var(--sky);text-transform:uppercase;white-space:nowrap}
.contact span{position:absolute;left:94px;top:36px;font-size:17.5px;color:var(--white);white-space:nowrap}
.copyright{position:absolute;left:0;top:388px;width:1200px;text-align:center;font-size:17.5px;color:var(--white)}
</style>
</head>
<body>
<div class="page">

  <header class="site-header">
    <div class="brand">
      <div class="brand-name">VORTEQ</div>
      <div class="brand-tag">Innovation &amp; Technical Services</div>
    </div>
    <nav class="nav">
      <a class="active" style="left:506px">Home</a>
      <a style="left:594px">About Us</a>
      <a style="left:736px">Our Products</a>
      <a style="left:940px">Contact Us</a>
    </nav>
  </header>

  <section class="hero">
    <div class="abs" style="left:560px;top:0;width:640px;height:554px" role="img" aria-label="Glowing blue network of connected nodes and digital data lines"></div>
    <h1 class="hero-title">Innovative<br>Designs Smart<br>Solutions</h1>
    <p class="hero-sub">Revolutionizing everyday products<br>with intelligent design and<br>cutting-edge engineering.</p>
    <a class="btn btn-hero">Discover Our Innovations</a>
  </section>

  <section class="about">
    <div class="about-visual" role="img" aria-label="Hand holding a glowing light bulb beneath a network of light lines"></div>
    <h2 class="section-title about-title">About Us</h2>
    <h3 class="about-sub">Engineering<br>innovation, one<br>product at a time</h3>
    <div class="about-copy">
      <p>At Vorteq, we are driven by curiosity and creativity. Our mission is to design and develop innovative solutions that simplify life, enhance efficiency, and introduce smarter ways to handle everyday tasks.</p>
      <p>From laundry accessories to pet care solutions, our team of engineers and designers is dedicated to shaping the future with practical, beautifully</p>
    </div>
    <a class="btn btn-read">Read More</a>
  </section>

  <section class="products">
    <h2 class="section-title products-title">Our Products</h2>

    <article class="card" style="left:114px">
      <div class="card-photo" role="img" aria-label="Person viewing a holographic garment display in a wardrobe" style="background:linear-gradient(135deg,#3a2a22 0%,#1c2530 50%,#2e6c8c 100%)"></div>
      <h3 class="card-name">The Hanger<br>Accessory</h3>
    </article>

    <article class="card card-open" style="left:445px">
      <h3>The Modern<br>Clothes Dryer</h3>
      <p>A revolutionary clothes drying solution that is energy-efficient, compact, and built for the modern home.</p>
    </article>

    <article class="card" style="left:776px">
      <div class="card-photo" role="img" aria-label="Person examining a small pet treat dispenser under purple light" style="background:linear-gradient(135deg,#7a3fd0 0%,#5b4fd8 50%,#3f7fd8 100%)"></div>
      <div class="ribbon">Coming Soon!</div>
      <h3 class="card-name">Patented Pet<br>Treat Dispenser</h3>
    </article>
  </section>

  <section class="why">
    <h2 class="section-title why-title">Why Choose<br>Vorteq?</h2>

    <div class="feature" style="top:2334px">
      <svg class="feature-icon" viewBox="0 0 72 72">
        <circle cx="36" cy="36" r="35" fill="#2a3aa0"/>
        <circle cx="36" cy="36" r="29" fill="none" stroke="#fff" stroke-width="1.2" stroke-dasharray="3 3"/>
        <path d="M36 20a10 10 0 0 0-6 18v5h12v-5a10 10 0 0 0-6-18z" fill="none" stroke="#fff" stroke-width="2"/>
        <path d="M31 47h10M32 51h8" stroke="#fff" stroke-width="2"/>
      </svg>
      <h4>Innovation First</h4>
      <p>We design solutions that enhance everyday life.</p>
    </div>

    <div class="feature" style="top:2430px">
      <svg class="feature-icon" viewBox="0 0 72 72">
        <circle cx="36" cy="36" r="35" fill="#2a3aa0"/>
        <circle cx="36" cy="36" r="29" fill="none" stroke="#fff" stroke-width="1.2" stroke-dasharray="3 3"/>
        <circle cx="40" cy="36" r="11" fill="none" stroke="#fff" stroke-width="2"/>
        <circle cx="40" cy="36" r="5" fill="none" stroke="#fff" stroke-width="2"/>
        <circle cx="25" cy="28" r="3" fill="none" stroke="#fff" stroke-width="2"/>
        <path d="M21 40h8M21 45h8" stroke="#fff" stroke-width="2"/>
      </svg>
      <h4>Sleek &amp; Functional</h4>
      <p>Our products are built for efficiency and elegance.</p>
    </div>

    <div class="feature" style="top:2527px">
      <svg class="feature-icon" viewBox="0 0 72 72">
        <circle cx="36" cy="36" r="35" fill="#2a3aa0"/>
        <circle cx="36" cy="36" r="29" fill="none" stroke="#fff" stroke-width="1.2" stroke-dasharray="3 3"/>
        <circle cx="36" cy="36" r="13" fill="none" stroke="#fff" stroke-width="2"/>
        <circle cx="36" cy="36" r="6" fill="none" stroke="#fff" stroke-width="2"/>
        <path d="M36 18v8M36 46v8M18 36h8M46 36h8" stroke="#fff" stroke-width="2"/>
      </svg>
      <h4>Future-Focused</h4>
      <p>We continuously develop new engineering-based solutions.</p>
    </div>

    <a class="btn btn-join">Join Our Journey</a>

    <div class="why-visual" role="img" aria-label="Engineer studying glowing holographic data charts"></div>
  </section>

  <footer class="site-footer">
    <div class="footer-brand">
      <div class="brand-name">VORTEQ</div>
      <div class="brand-tag">Innovation &amp; Technical Services</div>
    </div>

    <div class="contact" style="left:104px">
      <svg class="contact-icon" viewBox="0 0 72 72">
        <circle cx="36" cy="36" r="35" fill="#2a3aa0"/>
        <circle cx="36" cy="36" r="29" fill="none" stroke="#fff" stroke-width="1.2" stroke-dasharray="3 3"/>
        <path d="M36 52s-11-12-11-20a11 11 0 0 1 22 0c0 8-11 20-11 20z" fill="none" stroke="#fff" stroke-width="2"/>
        <circle cx="36" cy="32" r="4" fill="none" stroke="#fff" stroke-width="2"/>
      </svg>
      <h5>Address</h5>
      <span>1258&nbsp; enim ipsam voluptatem</span>
    </div>

    <div class="contact" style="left:478px">
      <svg class="contact-icon" viewBox="0 0 72 72">
        <circle cx="36" cy="36" r="35" fill="#2a3aa0"/>
        <circle cx="36" cy="36" r="29" fill="none" stroke="#fff" stroke-width="1.2" stroke-dasharray="3 3"/>
        <path d="M26 23l6-2 4 9-4 3a18 18 0 0 0 8 8l3-4 9 4-2 6c-14 1-25-10-24-24z" fill="none" stroke="#fff" stroke-width="2" stroke-linejoin="round"/>
      </svg>
      <h5>Call Us</h5>
      <span>+1 (888) 888-8888</span>
    </div>

    <div class="contact" style="left:779px">
      <svg class="contact-icon" viewBox="0 0 72 72">
        <circle cx="36" cy="36" r="35" fill="#2a3aa0"/>
        <circle cx="36" cy="36" r="29" fill="none" stroke="#fff" stroke-width="1.2" stroke-dasharray="3 3"/>
        <rect x="22" y="26" width="28" height="20" fill="none" stroke="#fff" stroke-width="2"/>
        <path d="M22 26l14 12 14-12" fill="none" stroke="#fff" stroke-width="2"/>
      </svg>
      <h5>Email Us</h5>
      <span>info@vorteq.com</span>
    </div>

    <p class="copyright">Copyright © 2025 Vorteq. All Rights Reserved</p>
  </footer>

</div>
</body>
</html>
```